I am looking for a flyer design for my upcoming symposium. Here are the details for the flyer and pictures of speakers are attached.

Name of Symposium: Lattice and Pathway Biosciences Symposium, Sponsored by the Corvale Chromatin Institute and the Department of Bioengineering
Date: January 8, 2018
Location: Havergill Auditorium, Tarnby Center for Applied Discovery, 2175 Orchard Terrace Ave, Philadelphia, PA 19127

Reception to follow after the symposium.

Also, please add - Register and upload abstracts for the symposium at www.qzvmrk.com. Registration and abstract submission closes on January 4, 2018.

Keynote Speaker:
Marthe Quillon, Ph.D.
NTVO Director General; Professor, Lyceum of Norvane; Director, Genetics and Developmental Biology at Institut Bramoux
Lyceum of Norvane, NTVO, Institut Bramoux
"Title of talk TBA."

Speakers:
Lena Drewcott, Ph.D.
Assistant Professor of Cell and Developmental Biology
Halvering State University, HMCS
"Title of talk TBA."

Paul Marden, Ph.D.
Assistant Professor of Genetics
"Title of talk TBA."

Ilse Varga, Ph.D.
Professor, Ostrander University
Otto Wenzlau Center for Molecular Medicine
"Title of talk TBA."

Jun Hao, Ph.D.
Professor of Cellular and Molecular Medicine
Coastal Meridian University
"Title of talk TBA."

Wei Lun, Ph.D.
Associate Professor of Pediatrics
The Youth Medical Pavilion of Philadelphia
"Spatial genome re-organization between fetal and adult hematopoietic stem cells."

Mei Zhou, Ph.D.
Professor, Department of Genetics
Ellsworth Medical School
"Title of talk TBA."

```html
<!DOCTYPE html>
<html lang="en">
<head>
<meta charset="utf-8">
<title>Lattice and Pathway Biosciences Symposium</title>
<link href="https://fonts.googleapis.com/css2?family=Oswald:wght@400;500&display=swap" rel="stylesheet">
<style>
  :root {
    --sky-light: #8fdcf2;
    --sky: #5cc8ec;
    --sky-deep: #2fb2dd;
    --teal: #1590ad;
    --ink: #0e5d72;
    --white: #ffffff;
    --photo-a: #c9d8de;
    --photo-b: #8aa4ae;
  }
  * { margin: 0; padding: 0; box-sizing: border-box; }
  html, body { width: 1040px; height: 1200px; overflow: hidden; background: #eef1f3; }
  body { font-family: "Oswald", sans-serif; }

  .flyer {
    position: relative; width: 1040px; height: 1200px; overflow: hidden;
    background:
      radial-gradient(ellipse 60% 45% at 62% 72%, rgba(120,228,255,.75), transparent 70%),
      linear-gradient(160deg, var(--sky-deep) 0%, var(--sky-light) 45%, var(--sky) 100%);
    color: var(--ink);
  }
  .abs { position: absolute; }

  .title {
    top: 58px; left: 0; width: 100%; text-align: center;
    color: var(--white); font-size: 41px; font-weight: 500; letter-spacing: .3px;
  }

  /* Sponsor band */
  .sponsor { top: 152px; left: 89px; width: 862px; height: 121px; display: flex; }
  .sponsor-label {
    width: 316px; background: var(--teal); border-top-left-radius: 60px;
    color: var(--white); font-size: 28px; font-weight: 500;
    display: flex; align-items: center; justify-content: center;
  }
  .sponsor-marks {
    flex: 1; background: var(--white); border-bottom-right-radius: 60px;
    display: flex; align-items: center; justify-content: center; gap: 30px;
  }
  .sponsor-name { display: flex; align-items: center; gap: 12px; font-size: 22px; font-weight: 500; line-height: 1.15; color: var(--ink); }
  .dot { flex: none; width: 22px; height: 22px; border-radius: 50%; background: var(--teal); }
  .square { flex: none; width: 22px; height: 22px; background: var(--teal); }
  .divider { width: 2px; height: 72px; background: var(--teal); }

  /* Section headings */
  .heading { top: 312px; font-size: 32px; font-weight: 500; display: flex; align-items: center; gap: 12px; }
  .heading::before, .heading::after { content: ""; height: 2px; background: var(--ink); flex: 1; }
  .heading.keynote { left: 43px; width: 340px; }
  .heading.speakers { left: 427px; width: 570px; gap: 18px; }

  .photo {
    background: linear-gradient(150deg, var(--photo-a), var(--photo-b));
    border: 2px solid var(--ink);
  }
  .keynote-photo { top: 368px; left: 76px; width: 288px; height: 240px; border-radius: 18px 50% 50% 50%; }

  .keynote-info { top: 622px; left: 68px; width: 340px; }
  .keynote-info .name { font-size: 34px; font-weight: 400; line-height: 1.2; }
  .keynote-info .role { font-size: 15.5px; line-height: 1.3; margin-top: 6px; width: 225px; }
  .keynote-info .org { font-size: 19px; margin-top: 6px; }
  .keynote-info .talk { font-size: 15px; margin-top: 2px; }
  .keynote-info .reception { font-size: 17px; font-weight: 500; margin-top: 16px; }

  /* Speaker grid */
  .speaker { width: 190px; }
  .speaker .photo { width: 163px; height: 136px; border-radius: 50% 50% 50% 50% / 55% 55% 45% 45%; border-top-left-radius: 14px; }
  .speaker .name { font-size: 18px; margin-top: 9px; line-height: 1.1; }
  .speaker .role { font-size: 10.5px; line-height: 1.3; margin-top: 3px; }
  .speaker .org { font-size: 11.5px; line-height: 1.3; margin-top: 2px; }
  .speaker .talk { font-size: 10.5px; line-height: 1.25; margin-top: 1px; }

  /* Date and location band */
  .event { top: 881px; left: 89px; width: 862px; height: 121px; display: flex; }
  .event-date {
    width: 316px; background: var(--white); border-top-left-radius: 60px;
    font-size: 35px; font-weight: 500; display: flex; align-items: center; justify-content: center;
  }
  .event-place {
    flex: 1; background: var(--teal); border-top-right-radius: 60px;
    color: var(--white); text-align: center; font-size: 20px; line-height: 1.25;
    display: flex; flex-direction: column; justify-content: center;
  }
  .event-place .label { font-size: 19px; font-weight: 500; }

  /* Registration band */
  .register { top: 1027px; left: 89px; width: 862px; height: 128px; display: flex; }
  .register-text {
    width: 545px; background: var(--teal); border-bottom-left-radius: 60px;
    color: var(--white); font-size: 20.5px; display: flex; flex-direction: column;
    justify-content: center; align-items: flex-end; padding-right: 22px;
  }
  .register-text span { padding: 6px 0; }
  .register-text span:first-child { border-bottom: 2px solid var(--white); }
  .register-detail {
    flex: 1; background: var(--white); border-top-right-radius: 60px;
    display: flex; flex-direction: column; justify-content: center; align-items: center;
    font-size: 29px; font-weight: 500; line-height: 1.15;
  }
  .register-detail span:first-child { border-bottom: 2px solid var(--ink); padding: 0 4px 2px; }
</style>
</head>
<body>
<main class="flyer">
  <h1 class="abs title">Lattice and Pathway Biosciences Symposium</h1>

  <section class="abs sponsor">
    <div class="sponsor-label">SPONSORED BY</div>
    <div class="sponsor-marks">
      <div class="sponsor-name"><span class="dot"></span><span>Corvale Chromatin<br>Institute</span></div>
      <div class="divider"></div>
      <div class="sponsor-name"><span class="square"></span><span>Department of<br>Bioengineering</span></div>
    </div>
  </section>

  <h2 class="abs heading keynote">KEYNOTE SPEAKER</h2>
  <h2 class="abs heading speakers">OUR SPEAKER</h2>

  <div class="abs photo keynote-photo" role="img" aria-label="Portrait photo of keynote speaker Marthe Quillon"></div>
  <div class="abs keynote-info">
    <p class="name">Marthe Quillon, Ph.D</p>
    <p class="role">NTVO Director General; Professor, Lyceum of Norvane; Director, Genetics and Developmental Biology at Institut Bramoux</p>
    <p class="org">Lyceum of Norvane, NTVO, Institut Bramoux</p>
    <p class="talk">"Title of talk TBA."</p>
    <p class="reception">Reception to follow after the symposium.</p>
  </div>

  <article class="abs speaker" style="top:380px;left:427px">
    <div class="photo" role="img" aria-label="Portrait photo of Lena Drewcott"></div>
    <p class="name">Lena Drewcott, Ph.D.</p>
    <p class="role">Assistant Professor of Cell and<br>Developmental Biology</p>
    <p class="org">Halvering State University, HMCS</p>
    <p class="talk">"Title of talk TBA."</p>
  </article>
  <article class="abs speaker" style="top:380px;left:626px">
    <div class="photo" role="img" aria-label="Portrait photo of Paul Marden"></div>
    <p class="name">Paul Marden, Ph.D.</p>
    <p class="role">Assistant Professor of Genetics</p>
    <p class="org">Halvering State University, HMCS</p>
    <p class="talk">"Title of talk TBA."</p>
  </article>
  <article class="abs speaker" style="top:380px;left:834px">
    <div class="photo" role="img" aria-label="Portrait photo of Ilse Varga"></div>
    <p class="name">Ilse Varga, Ph.D.</p>
    <p class="role">Professor, Ostrander University</p>
    <p class="org">Otto Wenzlau Center for<br>Molecular Medicine</p>
    <p class="talk">"Title of talk TBA."</p>
  </article>
  <article class="abs speaker" style="top:624px;left:427px">
    <div class="photo" role="img" aria-label="Portrait photo of Jun Hao"></div>
    <p class="name">Jun Hao, Ph.D.</p>
    <p class="role">Professor of Cellular and<br>Molecular Medicine</p>
    <p class="org">Coastal Meridian University</p>
    <p class="talk">"Title of talk TBA."</p>
  </article>
  <article class="abs speaker" style="top:624px;left:626px">
    <div class="photo" role="img" aria-label="Portrait photo of Wei Lun"></div>
    <p class="name">Wei Lun, Ph.D.</p>
    <p class="role">Associate Professor of Pediatrics</p>
    <p class="org">The Youth Medical Pavilion of Philadelphia</p>
    <p class="talk">"Spatial genome re-organization between fetal and adult hematopoietic stem cells."</p>
  </article>
  <article class="abs speaker" style="top:624px;left:834px">
    <div class="photo" role="img" aria-label="Portrait photo of Mei Zhou"></div>
    <p class="name">Mei Zhou, Ph.D.</p>
    <p class="role">Professor, Department of Genetics</p>
    <p class="org">Ellsworth Medical School</p>
    <p class="talk">"Title of talk TBA."</p>
  </article>

  <section class="abs event">
    <div class="event-date">January 8, 2018</div>
    <div class="event-place">
      <span class="label">LOCATION :</span>
      <span>Havergill Auditorium,</span>
      <span>Tarnby Center for Applied Discovery,</span>
      <span>2175 Orchard Terrace Ave, Philadelphia, PA 19127</span>
    </div>
  </section>

  <section class="abs register">
    <div class="register-text">
      <span>Register and upload abstracts for the symposium at</span>
      <span>Registration and abstract submission closes on</span>
    </div>
    <div class="register-detail">
      <span>www.qzvmrk.com</span>
      <span>January 4, 2018.</span>
    </div>
  </section>
</main>
</body>
</html>
```